CraneHollow - Business Card and Letterhead

After having received some fantastic submissions in our recent logo design project, I would now like to extend our branding to letterheads and business cards.
CraneHollow is a consulting service in the Construction Industry. We deal with both residential and commercial projects, and our clients include Architects, Builders, Tradespeople and Home Owners.
The designs should be simple and effective, convey personal service and professionalism, and display some level of creativity.
For both the business cards and letterhead, a white card stock will be used. This project is for business cards and letterheads only. Our new logo is attached for use.
The designs should incorporate our two main colours which are Blue (RGB 14,92,143) and Green (RGB 132,194,37).
For the time being, please submit all designs showing generic information including name, mobile number, email, postal address and website details. No fax number or physical address is required. I will provide our actual contact details once a final design has been selected.
I encourage you to interpret this brief in your own creative way, and look forward to some quality submissions.
Thanks!
Leo
CraneHollow.

```html
<!DOCTYPE html>
<html lang="en">
<head>
<meta charset="utf-8">
<title>CraneHollow Letterhead</title>
<link href="https://fonts.googleapis.com/css2?family=Source+Sans+3:wght@400;600;700&display=swap" rel="stylesheet">
<style>
  :root {
    --paper: #ffffff;
    --band-green: #b5c98f;
    --ink-navy: #2c3a55;
    --accent-green: #8cb35c;
    --brand-blue: #0e5c8f;
    --brand-green: #84c225;
  }
  html, body {
    margin: 0;
    padding: 0;
    overflow: hidden;
    background: var(--paper);
  }
  .letterhead {
    position: relative;
    width: 848px;
    height: 1200px;
    background: var(--paper);
    overflow: hidden;
    font-family: "Source Sans 3", "Myriad Pro", sans-serif;
  }
  .side-band {
    position: absolute;
    background: var(--band-green);
  }
  .side-band--upper {
    left: 26px;
    top: 0;
    width: 112px;
    height: 958px;
    border-radius: 0 0 4px 4px;
  }
  .side-band--lower {
    left: 28px;
    top: 1022px;
    width: 113px;
    height: 178px;
    border-radius: 4px 4px 0 0;
  }
  .brand {
    position: absolute;
    left: 24px;
    top: 978px;
    display: flex;
    align-items: center;
    gap: 5px;
  }
  .brand__mark {
    width: 10px;
    height: 10px;
    background: var(--brand-green);
  }
  .brand__name {
    font-size: 18px;
    font-weight: 700;
    color: var(--brand-blue);
    letter-spacing: -0.2px;
  }
  .contact {
    position: absolute;
    left: 150px;
    right: 20px;
    top: 44px;
    text-align: center;
  }
  .contact__address {
    margin: 0;
    font-size: 14px;
    color: var(--ink-navy);
    white-space: nowrap;
  }
  .contact__email {
    margin: 3px 0 0;
    font-size: 16.5px;
    color: var(--accent-green);
  }
</style>
</head>
<body>
  <main class="letterhead">
    <div class="side-band side-band--upper"></div>

    <header class="contact">
      <p class="contact__address">No.12, Harbour Lane, East Block, Karaikal, India- 609602 Ph: +91 0436 2251907 ,Mob: +91 9004718265</p>
      <p class="contact__email">e-mail: cranehollow@example.com</p>
    </header>

    <div class="brand">
      <span class="brand__mark"></span>
      <span class="brand__name">CraneHollow</span>
    </div>

    <div class="side-band side-band--lower"></div>
  </main>
</body>
</html>
```